Design B2B Video-Website
Zielgruppe
Das entstehende Portal bietet Videos zum Streaming an und richtet sich an Geschäftskunden, stellt also einen Shop mit Login dar. Das Angebot der Videos ist offen einsehbar, das Streamen ist gegen Bezahlung im Shop zu erwerben.
Aufgabenstellung
Die Seite soll sich im Layout an postvogel-beispiel.com orientieren; das Farbschema angelehnt an folgende
Hexcodes:
#231f20, #60bb46 und #828282 (und ähnliche Töne). Sprache ist Deutsch.
1. Startseite/Allgemein
Die dortige Navigationsleiste oben soll etwas größer werden; wird erweitert duch ein Logo links (muss NICHT designt werden; bitte mit Platzhalter füllen); die Navigationsitems (Angebot, Preise, Über uns, FAQ, Blog), mit Farb-hover-Effekt, sollen eine Kombination aus kleine Icon und Text sein; auf der rechten Seite die Buttons "Anmelden" (nicht rot), "Login" und Suchfenster mit Lupe und "Suche". Ein Zusatzmenü wie beim Klick auf "More"
soll mitdesigned werden (Items können Platzhalter sein).
Im Hauptteil eine Box mit Auflistung von Videos (auch zum Ansehen).
Die Seite enthält ebenso einen deutlichen Footer (umfangreicher).
2. Unterseite
Inhalt der Unterseite kann beispielhaft von "Features" bzw. "Pricing" entnommen werden. Dazu hell-grauer Hintergrund (verlaufend), mit eingepassten Bildern.
"Login"-Fenster bzw. "Anmelden" ähnlich zu Postvogel; mehr Felder und Farbschema siehe oben.
3.Login-Bereich
Im Login-Bereich (sprich wenn der Nutzer eingeloggt ist), soll die Navigation (mit anderen Items) nach links wandern und vertikal angeordnet werden. Im Hauptinhalt(rechts von der Navigation) sollen dann die Videos oder anderen Inhalte dargestellt werden.

```html
<!DOCTYPE html>
<html lang="de">
<head>
<meta charset="utf-8">
<title>Video B2B Webseite</title>
<link rel="stylesheet" href="https://fonts.googleapis.com/css2?family=Arimo:wght@400;700&display=swap">
<style>
:root{
  --green:#5bb846;
  --green-dark:#2f5a2a;
  --ink:#231f20;
  --grey:#828282;
  --grey-text:#6e6e6e;
  --header-bg:#ececec;
  --band:#d4d4d4;
  --line:#c8c8c8;
  --white:#ffffff;
}
*{box-sizing:border-box;margin:0;padding:0}
html,body{width:1200px;height:1088px;overflow:hidden}
body{position:relative;font-family:"Arimo",Arial,sans-serif;color:var(--grey-text);
  background:linear-gradient(to bottom,var(--white) 0,var(--white) 560px,#f1f1f1 690px,var(--band) 690px,var(--band) 908px,var(--white) 908px)}
.abs{position:absolute}
/* header */
.site-header{position:absolute;left:0;top:0;width:1200px;height:112px;background:var(--header-bg)}
.logo{position:absolute;left:80px;top:28px;font-size:24px;line-height:28px;color:var(--green-dark);letter-spacing:.5px}
.main-nav{position:absolute;left:0;top:0;height:112px}
.nav-item{position:absolute;top:0;height:112px;display:flex;align-items:center;gap:8px;font-size:14px;color:var(--ink);padding-top:24px;letter-spacing:.3px}
.nav-item.is-active{background:var(--green);color:var(--white);padding-left:14px;width:104px}
.nav-icon{width:20px;height:20px;border-radius:50%;background:#d9d9d9;border:1px solid #9a9a9a;display:flex;align-items:center;justify-content:center}
.nav-icon svg{width:11px;height:11px}
.btn-register{position:absolute;left:1007px;top:26px;width:100px;height:24px;background:var(--green);color:var(--ink);font-size:12px;display:flex;align-items:center;justify-content:center;gap:5px;box-shadow:1px 2px 2px rgba(0,0,0,.2)}
.search{position:absolute;left:1007px;top:58px;width:100px;height:26px;background:var(--white);font-size:11px;color:#9a9a9a;display:flex;align-items:center;gap:5px;padding-left:8px;box-shadow:1px 2px 2px rgba(0,0,0,.15)}
/* hero */
.welcome{position:absolute;left:0;top:176px;width:1200px;text-align:center;font-size:16px;font-weight:700;color:var(--grey);letter-spacing:.6px}
.welcome .dots{color:var(--green);letter-spacing:1px}
.people{position:absolute;background:linear-gradient(90deg,#7f9a85,#a7b7a9 40%,#8fa294);opacity:.8}
.video-card{position:absolute;left:290px;top:217px;width:616px;height:641px;background:var(--white);border:1px solid var(--line);box-shadow:4px 4px 6px rgba(0,0,0,.25)}
.player{position:absolute;left:40px;top:34px;width:535px;height:295px;background:linear-gradient(90deg,#8a7466 0,#b59c88 25%,#d5d5d5 45%,#bdbdbd 75%,#8e8e8e 100%)}
.play-btn{position:absolute;left:253px;top:119px}
.controls{position:absolute;left:40px;top:329px;width:535px;height:26px;background:#e8e8e8}
.track{position:absolute;left:18px;top:13px;width:498px;height:1px;background:#c5c5c5}
.track-done{position:absolute;left:18px;top:12px;width:145px;height:2px;background:#777}
.knob{position:absolute;left:27px;top:4px;width:18px;height:18px;border-radius:50%;background:var(--green)}
.video-title{position:absolute;left:38px;top:372px;font-size:12px;letter-spacing:.8px;color:var(--grey-text)}
.video-desc{position:absolute;left:38px;top:391px;width:540px;font-size:12px;line-height:14.5px;color:var(--grey-text)}
.more-head{position:absolute;left:38px;top:457px;font-size:12px;letter-spacing:.8px}
.more-item{position:absolute;left:38px;width:540px;height:34px}
.thumb{position:absolute;left:0;top:0;width:60px;height:34px}
.more-item h4{position:absolute;left:82px;top:4px;font-weight:400;font-size:12px}
.more-item p{position:absolute;left:82px;top:19px;font-size:12px;white-space:nowrap}
/* footer */
.footer-rule{position:absolute;top:936px;width:1px;height:118px;background:#888}
.foot-head{position:absolute;top:952px;font-size:14px;font-weight:700;color:var(--grey);letter-spacing:.3px}
.foot-link{position:absolute;left:375px;font-size:12px;color:var(--grey-text)}
.foot-note{position:absolute;left:524px;top:970px;font-size:9px;line-height:12px;color:var(--grey-text)}
.mail-input{position:absolute;left:524px;top:1005px;width:100px;height:25px;border:1px solid #bbb;border-radius:2px;font-size:8px;font-style:italic;color:#888;padding:9px 0 0 6px}
.social{position:absolute;top:953px;width:50px;text-align:center;font-size:7px;color:var(--grey-text)}
.social span{display:block;width:28px;height:28px;margin:0 auto 2px;border-radius:50%;background:linear-gradient(#9a9a9a,#6a6a6a)}
.page-end{position:absolute;left:0;top:1086px;width:1200px;height:1px;background:#999}
</style>
</head>
<body>
<header class="site-header">
  <div class="logo">VIDEO B2B<br>WEBSEITE</div>
  <nav class="main-nav">
    <div class="nav-item" style="left:290px"><span class="nav-icon"><svg viewBox="0 0 10 10"><rect x="1" y="1" width="8" height="8" fill="#555"/></svg></span>ANGEBOT</div>
    <div class="nav-item is-active" style="left:396px"><span class="nav-icon"><svg viewBox="0 0 10 10"><rect x="2" y="1" width="6" height="8" fill="#555"/></svg></span>PREISE</div>
    <div class="nav-item" style="left:513px"><span class="nav-icon"><svg viewBox="0 0 10 10"><circle cx="5" cy="3.5" r="2" fill="#333"/><path d="M1.5 9a3.5 3 0 0 1 7 0z" fill="#333"/></svg></span>ÜBER UNS</div>
    <div class="nav-item" style="left:644px"><span class="nav-icon" style="font-size:11px;font-weight:700">?</span>FAQ</div>
    <div class="nav-item" style="left:731px"><span class="nav-icon"><svg viewBox="0 0 10 10"><ellipse cx="5" cy="4.5" rx="3.5" ry="2.8" fill="none" stroke="#333" stroke-width="1.3"/></svg></span>BLOG</div>
    <div class="nav-item" style="left:827px"><span class="nav-icon"><svg viewBox="0 0 10 10"><rect x="2" y="4.5" width="6" height="4.5" fill="#333"/><path d="M3.3 4.5V3a1.7 1.7 0 0 1 3.4 0v1.5" fill="none" stroke="#333"/></svg></span>LOGIN</div>
  </nav>
  <div class="btn-register"><svg width="11" height="11" viewBox="0 0 10 10"><rect x="1" y="2" width="6" height="7" fill="none" stroke="#231f20"/><path d="M4 6l5-5" stroke="#231f20" stroke-width="1.4"/></svg>ANMELDEN</div>
  <div class="search"><svg width="10" height="10" viewBox="0 0 10 10"><circle cx="6" cy="4" r="2.8" fill="none" stroke="#999" stroke-width="1.3"/><path d="M4 6L1 9" stroke="#999" stroke-width="1.6"/></svg>SUCHE</div>
</header>

<h1 class="welcome"><span class="dots">●●●</span> WILLKOMMEN AUF UNSERER VIDEO-STREAMING PLATTFORM <span class="dots">●●●</span></h1>

<div class="people" role="img" aria-label="Silhouetten von Geschäftsleuten" style="left:25px;top:395px;width:265px;height:345px"></div>
<div class="people" role="img" aria-label="Silhouetten von Geschäftsleuten beim Handschlag" style="left:906px;top:390px;width:244px;height:350px"></div>

<main class="video-card">
  <div class="player" role="img" aria-label="Standbild des Videos: Frau im Profil">
    <svg class="play-btn" width="62" height="62" viewBox="0 0 62 62"><circle cx="31" cy="31" r="30" fill="rgba(255,255,255,.15)" stroke="#5bb846" stroke-width="1.5"/><path d="M16 17L50 31L16 45z" fill="#5bb846"/></svg>
  </div>
  <div class="controls"><div class="track"></div><div class="track-done"></div><div class="knob"></div></div>
  <div class="video-title">TITEL LORE IPSUM LORE IPSUM</div>
  <p class="video-desc">Lorem ipsum dolor sit amet, consetetur sadipscing elitr, sed diam nonumy eirmod tempor invidunt ut labore et dolore magna aliquyam erat, sed diam voluptua. At vero eos et accusam et justo duo dolores et ea rebum. Stet clita kasd gubergren,</p>
  <div class="more-head">WEITERE TITEL</div>
  <div class="more-item" style="top:482px"><div class="thumb" role="img" aria-label="Vorschaubild Titel 1" style="background:#1f3a1c"></div><h4>Titel 1</h4><p>Consetetur sadipscing elitr, sed diam nonumy eirmod mpor invidunt ut labore ...</p></div>
  <div class="more-item" style="top:526px"><div class="thumb" role="img" aria-label="Vorschaubild Titel 2" style="background:#3b3a40"></div><h4>Titel 2</h4><p>Consetetur sadipscing elitr, sed diam nonumy eirmod mpor invidunt ut labore ...</p></div>
  <div class="more-item" style="top:571px"><div class="thumb" role="img" aria-label="Vorschaubild Titel 3" style="background:#a8856a"></div><h4>Titel 3</h4><p>Consetetur sadipscing elitr, sed diam nonumy eirmod mpor invidunt ut labore ...</p></div>
</main>

<footer>
  <div class="footer-rule" style="left:289px"></div>
  <div class="footer-rule" style="left:907px"></div>
  <div class="foot-head" style="left:375px">LINKS</div>
  <div class="foot-link" style="top:979px">Kontakt</div>
  <div class="foot-link" style="top:998px">Impressum</div>
  <div class="foot-link" style="top:1017px">AGB</div>
  <div class="foot-head" style="left:524px">NEWSLETTER</div>
  <div class="foot-note">So sind Sie immer auf<br>dem Laufenden:</div>
  <div class="mail-input">Ihre E-Mail Adresse</div>
  <div class="social" style="left:703px"><span></span>Kreisnetz</div>
  <div class="social" style="left:744px"><span></span>Berufsring</div>
  <div class="social" style="left:785px"><span></span>Zwitscherpost</div>
  <div class="page-end"></div>
</footer>
</body>
</html>
```